Judicial election website to attract voters

I need a simple one-page web design for a judicial election. I'm going to put up one picture, maybe two. The picture I have needs a little touch-up (whiten teeth for example). I have 3 paragraphs of text. I'd like a "Donate" button that can link to a CoinDrift account. I'd also like a little background design, like the Constitution or something like that. There's a couple other little things but that's the bulk of it.

Target Market(s)

Involved voters and some media

Industry/Entity Type

Legal

Number of Pages Required

1 page

Font styles to use
Sans Serif

Requirements
Must have
• My picture, text, donate button
• Phrase "Remember to vote August 30, 2016!"
Nice to have
• Perhaps a second photo, maybe a short 30 second video of me talking directly to the voters, cool background: Constitution, something judgey.
Should not have
• Not sure ... profanity, I guess.

```html
<!DOCTYPE html>
<html lang="en">
<head>
<meta charset="utf-8">
<title>Marianne for Judge</title>
<link href="https://fonts.googleapis.com/css2?family=Lato:wght@300;400;700&display=swap" rel="stylesheet">
<style>
  :root {
    --ink: #1f3440;
    --body-text: #3f454b;
    --paper-light: #f6f6f7;
    --paper-mid: #e3e4e6;
    --campaign-red: #f44f4f;
    --white: #ffffff;
    --photo-warm: #8a5a36;
    --photo-navy: #1d2f66;
  }
  * { box-sizing: border-box; margin: 0; padding: 0; }
  html, body { width: 1200px; height: 1200px; overflow: hidden; }
  body { font-family: "Lato", sans-serif; background: var(--white); }

  .dedicated {
    position: relative;
    height: 606px;
    background: linear-gradient(160deg, var(--paper-mid) 0%, var(--paper-light) 45%, var(--paper-mid) 100%);
    text-align: center;
  }
  .dedicated__heading {
    position: absolute;
    top: 120px; left: 0; right: 0;
    font-weight: 700;
    font-size: 41px;
    letter-spacing: 0.5px;
    color: var(--ink);
  }
  .dedicated__text {
    position: absolute;
    top: 193px; left: 134px;
    width: 932px;
    font-weight: 300;
    font-size: 18px;
    line-height: 41.4px;
    color: var(--body-text);
    hyphens: auto;
  }

  .respected {
    position: relative;
    height: 594px;
    background: var(--campaign-red);
    overflow: hidden;
  }
  .respected__photo {
    position: absolute;
    left: 144px; top: 71px;
    width: 407px; height: 540px;
    background: linear-gradient(180deg, var(--photo-warm) 0%, var(--photo-navy) 100%);
  }
  .respected__heading {
    position: absolute;
    left: 610px; top: 62px;
    font-weight: 700;
    font-size: 40px;
    color: var(--white);
  }
  .respected__text {
    position: absolute;
    left: 612px; top: 137px;
    width: 462px;
    font-weight: 300;
    font-size: 18px;
    line-height: 41.4px;
    color: var(--white);
    hyphens: auto;
  }
</style>
</head>
<body>
  <section class="dedicated" role="img" aria-label="Faint background photo of a rolled parchment of the Constitution">
    <h2 class="dedicated__heading">DEDICATED</h2>
    <p class="dedicated__text">Dedicating her life to public service in central Florida, she has spent the last 18 years as a prosecutor fighting for victims of child abuse and sexual abuse in Orange and Osceola counties. &nbsp;She participates in local charities such as the Harvest Table Food Pantry and the Open Pages Reading League. &nbsp;Marianne shares her knowledge and experience freely, often mentoring the other young prosecutors and lecturing on jury selection and trial strategies. &nbsp;She is also committed to ensuring ethical behavior in the profession of law. &nbsp;In law school, she won an award for ethics and professionalism but since then she also served as Chair of a Regional Bar Grievance Committee, which handles complaints and ethical violations committed by local attorneys.</p>
  </section>

  <section class="respected">
    <div class="respected__photo" role="img" aria-label="Photo of a wooden judge's gavel resting on a Constitution scroll over an American flag"></div>
    <h2 class="respected__heading">RESPECTED</h2>
    <p class="respected__text">The cornerstone of Marianne’s candidacy for judge is her experience in the courtroom. &nbsp;Nobody knows how to run an efficient courtroom better than an attorney who has litigated a hundred felony jury trials and argued more pretrial motions than can be counted. &nbsp;But even a judge with all the right knowledge and experience cannot excel without the correct temperament.</p>
  </section>
</body>
</html>
```